Book Cover Design Project

I need a book cover for a book that we will be releasing in the next few months.

It is a business book aimed at small businesses and people who want to escape the 9 - 5 and start their own business.

We want it to look similar to: http://www.tolvanbrook.example/wp-content/uploads/2010/03/fold-up.jpg and also the book designs that I have uploaded images for.

I quite like the grey / charcoal background and the bright lime green colours from the Quiet Harbor logo that I have attached. However, anything bright would be good - I am prepared to be flexible with colours. The books I have attached are a high impact as well - being bright blue with white black font with a really cool font.

The book is titled:

The Lantern Shop Plan

By Dale Vortan

Still thinking of the tagline, for now just use "Start an Online Business in no time at all"

Room for a quote/testimonial on the front of the book at the bottom, and as well on the back.

For the back cover text just use dummy text and my photo that is attached for now as well.

Barcode ISBN on the back at the bottom - price will be $19.95

Needs to be in PSD so we can change the text from our end.

I really want to get a good template made that I can edit the text for as we are still developing the book, but I want to get the book cover done so I can start advertising that it will be arriving soon.

There will probably be alterations that I need help with later down the track so looking to work with someone closely on this, and I will pay you for any extra time down the track..

Sizes will probably be around: I think 20.5cm tall and 14cm wide would be good..

Not sure how thick for the spine, it will depend on how many words get cut off, but as an estimate probably 1.5CM..
Updates

Just added some more detail to the brief.. Please read it carefully.

Target Market(s)

small business owners, professionals who want to start their own business, soon to be entrepreneurs, entrepreneurs

Industry/Entity Type

Advertising

Requirements
Must have
• The Lantern Shop Plan

and Dale Vortan must be prominent.

Tag line should be look cool under the title.

Must be very modern and cool. Needs to catch people's eyes so needs to be really punchy.

Nice to have
• Maybe a clock or stopwatch icon would be cool to add in there so it isn't just plain.. Similar to like how the books have a cool icon with them that I have attached in the uploaded images.
Should not have
• I like simplicity, artistic and very high impact. It really needs to draw you in and catch your eye.

Don't use plain boring fonts. Although I like simplicity slick design is very important - I dont want it to be boring - it has to look high quality and expensive. Therefore do not use fonts like Arial, Times New Roman those really boring fonts that make it look cheap. If I was going to do something like that then I might as well do it myself.

If you want to see the quality of things that I am usually involved with look at the artwork for one of my events that I run called Daybreaker: http://www.daybreaker.example/daybreaker-festival-anthems-ft-loomsparrow-harvest-night-eve-metro-report/

That will give you an idea of what type of quality things that I am involved with, so you need to be up for the task..

```html
<!DOCTYPE html>
<html lang="en">
<head>
<meta charset="utf-8">
<title>The Lantern Shop Plan – Book Cover</title>
<link rel="stylesheet" href="https://fonts.googleapis.com/css2?family=Cabin:wght@500&family=Ubuntu:wght@500;700&display=swap">
<style>
  :root {
    --stage: #f1f1f1;
    --charcoal-top: #2c2c2c;
    --charcoal-mid: #3a3a3a;
    --fade-grey: #8a8a8a;
    --fade-light: #f4f4f4;
    --lime: #b6e51c;
    --lime-bright: #d4f53a;
    --lime-deep: #7fb313;
    --ink-dark: #1c2608;
    --author-white: #f2f2f2;
    --dial-silver: #c9c9c9;
    --dial-white: #fbfbfb;
  }
  * { margin: 0; padding: 0; box-sizing: border-box; }
  html, body {
    width: 1200px;
    height: 1000px;
    overflow: hidden;
    background: var(--stage);
  }
  .stage {
    position: relative;
    width: 1200px;
    height: 1000px;
  }
  .book-cover {
    position: absolute;
    left: 320px;
    top: 90px;
    width: 560px;
    height: 820px;
    overflow: hidden;
    background: linear-gradient(180deg,
      var(--charcoal-top) 0%,
      var(--charcoal-mid) 48%,
      var(--fade-grey) 72%,
      var(--fade-light) 94%,
      #ffffff 100%);
    box-shadow: 0 10px 30px rgba(0,0,0,0.18);
  }
  .author {
    position: absolute;
    top: 40px;
    left: 0;
    width: 100%;
    text-align: center;
    font-family: "Cabin", sans-serif;
    font-weight: 500;
    font-variant: small-caps;
    font-size: 30px;
    letter-spacing: 1px;
    color: var(--author-white);
  }
  .title {
    position: absolute;
    top: 100px;
    left: 0;
    width: 100%;
    text-align: center;
    font-family: "Ubuntu", sans-serif;
    font-weight: 500;
    text-transform: uppercase;
    color: var(--lime);
    line-height: 1;
  }
  .title-line {
    display: block;
    background: linear-gradient(180deg, var(--lime-bright) 0%, var(--lime) 60%, var(--lime-deep) 100%);
    -webkit-background-clip: text;
    background-clip: text;
    -webkit-text-fill-color: transparent;
  }
  .title-line--top { font-size: 60px; letter-spacing: 1px; }
  .title-line--main { font-size: 84px; letter-spacing: 1px; margin-top: 4px; }
  .tagline-ribbon {
    position: absolute;
    top: 280px;
    left: 0;
    width: 560px;
    height: 150px;
  }
  .tagline-ribbon svg { position: absolute; inset: 0; }
  .tagline {
    position: absolute;
    top: 30px;
    left: 0;
    width: 100%;
    text-align: center;
    font-family: "Ubuntu", sans-serif;
    font-weight: 700;
    color: var(--ink-dark);
    line-height: 1.05;
  }
  .tagline-line--one { display: block; font-size: 27px; }
  .tagline-line--two { display: block; font-size: 34px; }
  .stopwatch-art {
    position: absolute;
    left: 105px;
    top: 450px;
    width: 350px;
    height: 350px;
    border-radius: 50%;
    background: radial-gradient(circle at 50% 45%, var(--dial-white) 0%, var(--dial-white) 62%, var(--dial-silver) 80%, #9b9b9b 100%);
  }
</style>
</head>
<body>
  <main class="stage">
    <section class="book-cover" aria-label="Book cover: The Lantern Shop Plan by Dale Vortan">
      <p class="author">By Dale Vortan</p>
      <h1 class="title">
        <span class="title-line title-line--top">The Lantern</span>
        <span class="title-line title-line--main">Shop Plan</span>
      </h1>
      <div class="tagline-ribbon">
        <svg viewBox="0 0 560 150" width="560" height="150" aria-hidden="true">
          <defs>
            <linearGradient id="ribbonFace" x1="0" y1="0" x2="0" y2="1">
              <stop offset="0" stop-color="#d9f55a"/>
              <stop offset="0.5" stop-color="#b6e51c"/>
              <stop offset="1" stop-color="#86bd14"/>
            </linearGradient>
            <linearGradient id="ribbonTail" x1="0" y1="0" x2="0" y2="1">
              <stop offset="0" stop-color="#9fd01a"/>
              <stop offset="1" stop-color="#5f8a0d"/>
            </linearGradient>
          </defs>
          <path class="ribbon-tail" d="M14 72 L92 58 L100 128 L24 138 L50 104 Z" fill="url(#ribbonTail)"/>
          <path class="ribbon-tail" d="M546 72 L468 58 L460 128 L536 138 L510 104 Z" fill="url(#ribbonTail)"/>
          <path class="ribbon-fold" d="M80 112 L100 128 L96 104 Z" fill="#4c6f0a"/>
          <path class="ribbon-fold" d="M480 112 L460 128 L464 104 Z" fill="#4c6f0a"/>
          <path class="ribbon-band" d="M70 28 Q280 -8 490 28 L480 114 Q280 80 80 114 Z" fill="url(#ribbonFace)"/>
          <path d="M76 36 Q280 2 484 36" fill="none" stroke="#eafb9a" stroke-width="2" opacity="0.8"/>
          <path d="M84 106 Q280 72 476 106" fill="none" stroke="#eafb9a" stroke-width="2" opacity="0.6"/>
        </svg>
        <p class="tagline">
          <span class="tagline-line--one">Start an Online Business</span>
          <span class="tagline-line--two">in no time at all</span>
        </p>
      </div>
      <div class="stopwatch-art" role="img" aria-label="Silver stopwatch illustration with a lime green segment marking the first minutes"></div>
    </section>
  </main>
</body>
</html>
```